Financial Broker firm looking for Brochure design/Pdf-document

Job Type
Brochure Design/PDF-Document
Task Outline
Create a Brochure Design that also works for sending as pdf-document.
Task Description
We need a combined corporate brochure (Booklet style) to give out to potential clients as well as sending it to potential clients through Internet as pdf-document.
We need a background template with pictures and colors that gives the impression of professionalism, trustworthiness and seriousness. Attached text in English but the text will be translated into different languages to fit different markets. Therefore we would like to receive one template including the text and one without any text (but with the logo). Please inform us where (any) pictures and/or photos on the template have been taken from in order for us to buy and use them legally.
About Us
Our company Quelvant Partners AB is a financial brokerage company who provides a diversity of services for different selected partners (www.quelvantpartners.example).
Target Market
Companies on all levels, domestic or international
Requirements
Must Have:
-The text and logo attached below
Industry/Entity Type
Financial
Look and feel

```html
<!DOCTYPE html>
<html lang="en">
<head>
<meta charset="utf-8">
<title>Quelvant Partners – Brochure Page</title>
<link href="https://fonts.googleapis.com/css2?family=Arimo:wght@400;700&display=swap" rel="stylesheet">
<style>
  :root {
    --page: #ffffff;
    --rail: #dcdcdd;
    --ink: #231f20;
    --brand: #1a1a1a;
    --banner-dark: #1f5f99;
    --banner-mid: #3b86c4;
    --banner-light: #9fd0ec;
    --photo-dark: #2a2a2c;
    --photo-mid: #8a8a8e;
    --photo-light: #d9d9dc;
  }
  html, body {
    margin: 0;
    padding: 0;
    overflow: hidden;
    background: var(--page);
  }
  .page {
    position: relative;
    width: 849px;
    height: 1200px;
    overflow: hidden;
    background: var(--page);
    font-family: "Arimo", Arial, sans-serif;
    color: var(--ink);
  }
  .rail-left {
    position: absolute;
    left: 0; top: 0;
    width: 60px; height: 1200px;
    background: var(--rail);
  }
  .rail-right {
    position: absolute;
    left: 658px; top: 0;
    width: 191px; height: 1200px;
    background: var(--rail);
  }
  .brand {
    position: absolute;
    left: 120px; top: 50px;
    font-weight: 700;
    font-size: 33px;
    letter-spacing: 0.5px;
    color: var(--brand);
  }
  .banner {
    position: absolute;
    left: 68px; top: 163px;
    width: 668px; height: 56px;
    background: linear-gradient(90deg, var(--banner-dark) 0%, var(--banner-mid) 55%, var(--banner-light) 100%);
    border-top: 2px solid #ffffff;
    box-shadow: 0 0 0 1px #b9cfe0;
    display: flex;
    align-items: center;
    padding-left: 45px;
    box-sizing: border-box;
    color: #ffffff;
    font-weight: 700;
    white-space: nowrap;
  }
  .banner .big { font-size: 27px; }
  .banner .small { font-size: 18px; }
  .content {
    position: absolute;
    left: 120px; top: 256px;
    width: 616px;
    font-size: 12.6px;
    line-height: 17.7px;
  }
  .content p {
    margin: 0 0 9px;
    text-align: justify;
  }
  .content h2 {
    margin: 9px 0 3px;
    font-size: 13.4px;
    font-weight: 700;
  }
  .float-spacer {
    float: right;
    width: 0;
    height: 125px;
  }
  .photo {
    float: right;
    clear: right;
    width: 295px;
    height: 318px;
    margin: 0 0 8px 16px;
    background: radial-gradient(ellipse at 40% 45%, var(--photo-light) 0%, var(--photo-mid) 45%, var(--photo-dark) 100%);
  }
  .services {
    list-style: none;
    margin: 0 0 9px;
    padding: 0;
  }
  .services li::before {
    content: "\2022";
    margin-right: 4px;
  }
</style>
</head>
<body>
<div class="page">
  <div class="rail-left"></div>
  <div class="rail-right"></div>

  <div class="brand">QUELVANT PARTNERS</div>

  <div class="banner">
    <span class="big">“A&nbsp;PARTNER&nbsp;</span><span class="small">IN&nbsp;</span><span class="big">NEED&nbsp;AS&nbsp;</span><span class="small">IN&nbsp;</span><span class="big">SUCCESS”</span>
  </div>

  <div class="content">
    <div class="float-spacer"></div>
    <div class="photo" role="img" aria-label="Photo of a businesswoman holding out her hand with glowing currency symbols for euro, dollar, pound, yen and cent floating around her"></div>

    <p>As a finance broker based in Sweden, we market a diversity of services in order for you to improve your company’s finances and at the same time lowering your company’s cost. Through our partners, we will assist you to find the right solution, which includes best price and quality to fit your needs and demands. Our goal is customer satisfactory, our service is for free and our aim is through the knowledge and expertise we, we can build a strong long and lasting business relationship together. With Quelvant Partners you will have your own personal account manager (or reseller contact) that speaks the language you understand in order to take advantage of the services our partners provide. We are regulated by the Swedish financial inspection.</p>

    <h2>The services our partners provide are:</h2>
    <ul class="services">
      <li>Foreign exchange service</li>
      <li>Covering financial risks</li>
      <li>Trade credit insurance</li>
      <li>Bonding</li>
      <li>Trade debt collections</li>
      <li>Factoring</li>
    </ul>

    <h2>Foreign exchange service</h2>
    <p>If your company trades internationally, you are more than likely to make international payments. Our partners will help your company manage this process. You can save half the costs involved in the money transfer and get access to a better service compared to traditional banks.</p>

    <h2>Covering financial risks</h2>
    <p>With international payments you most likely have paid or received different amounts from foreign currencies. This is called fluctuations in the currency market. The service we provide will help you to identify risks and how you can cover them. We are working with different partners that will cover your currency risks. They can also assist you with avoiding commodity risks for your production, for example protecting the price of a production commodity or interest rate risks, if you have a variable loan. The burden of a rise in the interest rate may be expensive to your company. If you are interested, there is also the option by remunerate your liquidity through our partners’ cash certificate deposit.</p>

    <h2>Trade Credit Insurance</h2>
    <p>With a Trade Credit Insurance, you do not need to worry about your customers not being able to pay your bills or have to set aside funds for bad debts. Instead trade credit insurance provides a vital injection against non-payment of goods or services, both in the domestic as well as your export market. We know that many unpaid invoices are caused by insufficient knowledge about your customers’ solvency. In the event of insolvency or payment default, credit insurance gives you swift access to replacement capital without harming your balance sheet.</p>
  </div>
</div>
</body>
</html>
```